Criminal Defense law firm needs website and logo

Need a logo design and web design for a small firm in Miami, Florida. The firm concentrates in the areas of state and federal criminal defense in Miami Dade County, Florida.The firm handles cases in the areas of Drug Possession, Fraud Offenses, Traffic Offenses, domestic violence, Violent Crimes, probation violation, Juvenile Delinquency, and expunction/expungment of criminal records (detailed list provided in attachment). The name of the attorney is Loreta Benavides-Kurtz. Sole Practitioner. Will attach profile. (the attachment are from my previous law firm, can use any of the language but adjust to a sole practitioner)

Industry/Entity Type

Lawyer

Number of Pages Required

3 page

Font styles to use
Serif

Colors
0356a4

Requirements
Must have
• Page that includes area's of practice. Page for Attorney profile. Contact page indicating that we speak Spanish and accept all major credit cards.

```html
<!DOCTYPE html>
<html lang="en">
<head>
<meta charset="utf-8">
<title>Loreta Benavides-Kurtz | Criminal Defense</title>
<link rel="stylesheet" href="https://fonts.googleapis.com/css2?family=Montserrat:wght@500;600;700&family=Open+Sans:wght@400;600;700&display=swap">
<style>
:root{
  --brand:#2479b0;
  --brand-dark:#1d6699;
  --header-bg:#2b2b2b;
  --ink:#1a1a1a;
  --body-text:#555555;
  --muted:#9a9a9a;
  --welcome-bg:#e7e7e7;
  --white:#ffffff;
  --line:#b9b9b9;
  --icon:#333333;
}
*{margin:0;padding:0;box-sizing:border-box}
html,body{width:1200px;height:2267px;overflow:hidden}
body{position:relative;background:var(--white);font-family:"Open Sans",Arial,sans-serif;color:var(--body-text)}
.abs{position:absolute}
.heading{font-family:"Montserrat",Arial,sans-serif}

/* Top bar */
.top-bar{left:0;top:0;width:1200px;height:148px;background:var(--header-bg)}
.top-bar__info{top:47px;font-size:13px;color:var(--muted)}
.brand{left:466px;top:10px;display:flex;align-items:center;gap:12px}
.brand__mark{width:84px;height:84px;border-radius:50%;background:var(--brand);border:5px solid var(--white)}
.brand__name{font-family:"Montserrat",Arial,sans-serif;font-weight:500;color:var(--brand);font-size:20px;line-height:1.15;letter-spacing:.5px}

/* Navigation */
.main-nav{left:47px;top:106px;width:1103px;height:88px;background:var(--brand);border-radius:4px;display:flex;justify-content:center;align-items:center}
.main-nav a{font-family:"Montserrat",Arial,sans-serif;font-weight:700;font-size:14px;color:var(--white);text-decoration:none;padding:0 28px;white-space:nowrap}

/* Hero */
.hero{left:0;top:148px;width:1200px;height:589px;background:linear-gradient(90deg,#5d5550 0%,#6a4a3a 35%,#7a4c32 60%,#4a3530 100%)}
.hero__portrait{right:0;top:0;width:360px;height:589px;background:linear-gradient(180deg,#5a3a2c 0%,#7b5a48 45%,#2e3845 100%)}
.hero__title{right:367px;top:342px;text-align:right;font-size:50px;font-weight:600;color:var(--white);line-height:66px;white-space:nowrap}
.hero__text{left:180px;top:492px;width:660px;text-align:center;font-size:15px;line-height:23px;color:var(--white)}
.btn{display:flex;align-items:center;justify-content:center;background:var(--brand);color:var(--white);font-size:12px;text-transform:uppercase;border-radius:3px;text-decoration:none}
.hero__btn{left:690px;top:568px;width:136px;height:41px;border:2px solid #cfe3f2}
.slider-arrows{left:573px;top:707px;width:63px;height:30px;background:#f1f1f1;display:flex;justify-content:space-around;align-items:center}

/* Welcome */
.welcome{left:0;top:737px;width:1200px;height:291px;background:var(--welcome-bg)}
.section-title{width:1200px;left:0;text-align:center;font-size:33px;font-weight:600;color:var(--ink);white-space:nowrap}
.section-title span{color:var(--brand)}
.welcome__rule{top:805px;height:1px;background:var(--line)}
.welcome__title{top:784px;font-size:31px}
.welcome__text{left:130px;top:849px;width:940px;text-align:center;font-size:12px;line-height:22px}
.welcome__btn{left:533px;top:941px;width:132px;height:38px}

/* Practice areas */
.practice__title{top:1062px}
.area__label{height:103px;background:var(--brand);color:var(--white);font-family:"Montserrat",Arial,sans-serif;font-weight:600;font-size:18px;display:flex;align-items:center;padding-left:63px;white-space:nowrap}
.area__label--right{padding-left:30px}
.area__card{height:142px;border:1.5px solid var(--brand);background:var(--white);padding:22px 27px;font-size:14px;line-height:26px}
.area__card--right{text-align:right}
.area__arrow{width:36px;height:33px;background:var(--brand);border-radius:2px;display:flex;align-items:center;justify-content:center}
.dots{left:518px;top:1759px;display:flex;gap:13px}
.dots i{width:16px;height:16px;border-radius:50%;border:1.5px solid var(--brand);display:block}
.dots i.is-active{background:var(--brand)}

/* Testimonials */
.testimonials{left:0;top:1866px;width:1200px;height:333px;background:var(--brand)}
.testimonials__title{top:1912px;color:var(--white)}
.testimonials__quote{left:150px;top:1985px;width:900px;text-align:center;font-size:13px;line-height:27px;font-weight:600;color:var(--white)}
.testimonials__quote span{white-space:nowrap}
.quote-mark{position:absolute;font-family:Georgia,serif;font-size:42px;line-height:1;color:var(--white);font-style:italic}
.quote-mark--open{left:226px;top:1964px}
.quote-mark--close{left:838px;top:1998px}
.testimonials__author{top:2051px;left:0;width:1200px;text-align:center;font-family:"Montserrat",Arial,sans-serif;font-size:16px;color:var(--white)}
.client-thumb{top:2094px;width:65px;height:62px;border:2px solid var(--white);background:linear-gradient(180deg,#3a3a3a,#1f1f1f)}
.client-thumb--active{background:linear-gradient(180deg,#d8d8d8,#8e98a6)}

/* Footer */
.site-footer{left:0;top:2199px;width:1200px;height:68px;background:var(--white)}
.site-footer__copy{left:50px;top:2225px;font-size:12px;color:var(--ink)}
.social{left:982px;top:2236px;display:flex;gap:28px}
.social i{width:10px;height:10px;border-radius:50%;background:var(--icon);display:block}
</style>
</head>
<body>

<header class="top-bar abs"></header>
<div class="top-bar__info abs" style="left:154px">Email id : info@companyname.com</div>
<div class="brand abs">
  <div class="brand__mark"></div>
  <div class="brand__name">LORETA<br>BENAVIDES-KURTZ</div>
</div>
<div class="top-bar__info abs" style="left:822px">Call Us : 123-456-7890</div>

<section class="hero abs">
  <div class="hero__portrait abs" role="img" aria-label="Portrait photo of the attorney"></div>
</section>
<div class="hero abs" role="img" aria-label="Background photo of scales of justice in front of law books" style="width:840px;background:linear-gradient(90deg,rgba(90,85,80,.6),rgba(120,75,50,.4))"></div>

<nav class="main-nav abs">
  <a href="#">HOME</a>
  <a href="#">ABOUT US</a>
  <a href="#">AREA'S OF PRACTICE</a>
  <a href="#">ATTORNEY PROFILE</a>
  <a href="#">TESTIMONIALS</a>
  <a href="#">CONTACT US</a>
</nav>

<h1 class="hero__title heading abs">Lorem Ipsum Dolor Sit<br>Amet, Consectetur</h1>
<p class="hero__text abs">Lorem ipsum dolor sit amet, consectetur adipiscing elit, sed do eiusmod tempor incididunt ut ldolore magna aliqua. Ut enim ad minim veniam, quis nostrud exercitation laboris</p>
<a class="btn hero__btn abs" href="#">Read More</a>
<div class="slider-arrows abs">
  <svg width="10" height="14" viewBox="0 0 10 14"><path d="M8 1 2 7l6 6" fill="none" stroke="#111" stroke-width="2"/></svg>
  <svg width="10" height="14" viewBox="0 0 10 14"><path d="M2 1l6 6-6 6" fill="none" stroke="#111" stroke-width="2"/></svg>
</div>

<section class="welcome abs"></section>
<div class="welcome__rule abs" style="left:47px;width:208px"></div>
<div class="welcome__rule abs" style="left:945px;width:205px"></div>
<h2 class="section-title welcome__title heading abs">Welcome to <span>LORETA BENAVIDES-KURTZ</span></h2>
<p class="welcome__text abs">Lorem ipsum dolor sit amet, consectetur adipiscing elit, sed do eiusmod tempor incididunt ut labore et dolore magna aliqua. Ut enim ad minim veniam, quis nostrud exercitation ullamco laboris nisi ut aliquip ex ea commodo consequat. Duis aute irure dolor in reprehenderit in voluptate velit esse cillum dolore eu fugiat nulla pariatur. Excepteur sint occaecat cupidatat non proident, sunt in culpa qui officia deserunt mollit anim id est laborum.</p>
<a class="btn welcome__btn abs" href="#">Read More</a>

<h2 class="section-title practice__title heading abs">Areas <span>of Practise</span></h2>

<div class="area__label abs" style="left:65px;top:1159px;width:375px">Drug Possession</div>
<svg class="abs" style="left:440px;top:1193px" width="16" height="34" viewBox="0 0 16 34"><path d="M0 0 16 17 0 34z" fill="#2479b0"/></svg>
<div class="area__card abs" style="left:485px;top:1157px;width:648px">Lorem ipsum dolor sit amet, consectetur adipiscing elit, sed do eiusmod tempor incididunt ut labore et dolore magna aliqua. Ut enim ad minim veniam, quis nostrud exercitation ullamco laboris nisi ut aliquip ex ea commodo consequat.</div>
<div class="area__arrow abs" style="left:1068px;top:1282px"><svg width="10" height="14" viewBox="0 0 10 14"><path d="M2 1l6 6-6 6" fill="none" stroke="#fff" stroke-width="2"/></svg></div>

<div class="area__card area__card--right abs" style="left:66px;top:1354px;width:649px">Lorem ipsum dolor sit amet, consectetur adipiscing elit, sed do eiusmod tempor incididunt ut labore et dolore magna aliqua. Ut enim ad minim veniam, quis nostrud exercitation ullamco laboris nisi ut aliquip ex ea commodo consequat.</div>
<div class="area__arrow abs" style="left:104px;top:1478px"><svg width="10" height="14" viewBox="0 0 10 14"><path d="M8 1 2 7l6 6" fill="none" stroke="#fff" stroke-width="2"/></svg></div>
<svg class="abs" style="left:750px;top:1388px" width="16" height="34" viewBox="0 0 16 34"><path d="M16 0 0 17 16 34z" fill="#2479b0"/></svg>
<div class="area__label area__label--right abs" style="left:766px;top:1354px;width:384px">Passive House Certified Windows</div>

<div class="area__label abs" style="left:65px;top:1556px;width:375px">Traffic Offenses</div>
<svg class="abs" style="left:440px;top:1590px" width="16" height="34" viewBox="0 0 16 34"><path d="M0 0 16 17 0 34z" fill="#2479b0"/></svg>
<div class="area__card abs" style="left:485px;top:1555px;width:648px">Lorem ipsum dolor sit amet, consectetur adipiscing elit, sed do eiusmod tempor incididunt ut labore et dolore magna aliqua. Ut enim ad minim veniam, quis nostrud exercitation ullamco laboris nisi ut aliquip ex ea commodo consequat.</div>
<div class="area__arrow abs" style="left:1068px;top:1680px"><svg width="10" height="14" viewBox="0 0 10 14"><path d="M2 1l6 6-6 6" fill="none" stroke="#fff" stroke-width="2"/></svg></div>

<div class="dots abs"><i></i><i class="is-active"></i><i></i></div>

<section class="testimonials abs"></section>
<h2 class="section-title testimonials__title heading abs">Client Testimonials</h2>
<div class="quote-mark quote-mark--open">&ldquo;</div>
<p class="testimonials__quote abs"><span>Lorem ipsum dolor sit amet, consectetur adipiscing elit, sed do eiusmod tempor incididunt ut labore et dolore magna aliqua.</span><br><span>Ut enim ad minim veniam, quis nostrud exercitation ullamco laboris.</span></p>
<div class="quote-mark quote-mark--close">&rdquo;</div>
<div class="testimonials__author abs">- JOHN SMITH</div>
<div class="client-thumb abs" style="left:455px" role="img" aria-label="Client photo"></div>
<div class="client-thumb abs" style="left:535px" role="img" aria-label="Client photo"></div>
<div class="client-thumb client-thumb--active abs" style="left:615px" role="img" aria-label="Client photo"></div>
<div class="client-thumb abs" style="left:695px" role="img" aria-label="Client photo"></div>

<footer class="site-footer abs"></footer>
<div class="site-footer__copy abs">All Rights Reserved. Copyrights @Company Name. 2016</div>
<div class="social abs"><i></i><i></i><i></i><i></i><i></i></div>

</body>
</html>
```